Owen Tasker Studios Business Card

Looking for a clear, modern, elegant, sharp business card that conveys a professional yet edgy image to my business as a wedding, portrait, and travel photographer. Would like something that looks vintage yet modern. Need a new business card to grow my business. We are growing the business for Wedding and Event Photography as well as fine art Photography. (Mostly Landscapes)
Updates

I’m looking through designs now but I have a new logo that i want using please.

New logo uploaded please redesign using that

PLEASE ALL DESIGNERS LOOK IN BRIEF FOR NEW LOGO

Target Market(s)

Brides, Grooms, Families with Kids, People looking for Fine Art Photography Artwork

Industry/Entity Type

Photographer

Contact Information for Business Card

Unsure

Font styles to use
Serif

Colors

Designer to choose colors to be used in the design.

Requirements
Must have
• My Website:
• http://taskerlens.examplefolio.net
• Phone:
• 323-481-5206
• Email:
• owentaskerlens@mailbox-example.net
Nice to have
• Would like a sort of shine on the printing finish.
• I like black I think it looks good on a business card.
• Can try working with my logo (png that I've attached)

```html
<!DOCTYPE html>
<html lang="en">
<head>
<meta charset="utf-8">
<title>Owen Tasker Studios – Business Card</title>
<link href="https://fonts.googleapis.com/css2?family=Advent+Pro:wght@300&family=Arimo&family=Montserrat:wght@400&family=Open+Sans&display=swap" rel="stylesheet">
<style>
  :root {
    --page-bg: #b8b8b8;
    --card-top: #8c8c8c;
    --card-bottom: #323232;
    --ink: #ffffff;
    --ornament: rgba(255, 255, 255, 0.55);
    --shadow: rgba(0, 0, 0, 0.55);
  }
  * { margin: 0; padding: 0; box-sizing: border-box; }
  html, body {
    width: 993px;
    height: 1200px;
    overflow: hidden;
    background: var(--page-bg);
  }
  .canvas { position: relative; width: 993px; height: 1200px; }

  .card {
    position: absolute;
    left: 22px;
    width: 945px;
    height: 540px;
    background: linear-gradient(to bottom, var(--card-top), var(--card-bottom));
    box-shadow: 4px 6px 10px var(--shadow);
    color: var(--ink);
    overflow: hidden;
  }
  .card--front { top: 20px; }
  .card--back { top: 619px; }

  /* Wordmark */
  .wordmark {
    position: absolute;
    transform: translateX(-50%);
    text-align: center;
    font-family: "Montserrat", sans-serif;
    font-weight: 400;
    color: var(--ink);
    white-space: nowrap;
  }
  .wordmark__name { display: block; }
  .wordmark__sub { display: block; }

  .card--front .wordmark { left: 472px; top: 236px; }
  .card--front .wordmark__name { font-size: 34px; letter-spacing: 9px; line-height: 40px; padding-left: 9px; }
  .card--front .wordmark__sub { font-size: 12px; letter-spacing: 6px; margin-top: 14px; padding-left: 6px; }

  .card--back .wordmark { left: 746px; top: 242px; }
  .card--back .wordmark__name { font-size: 25px; letter-spacing: 6px; line-height: 30px; padding-left: 6px; }
  .card--back .wordmark__sub { font-size: 10px; letter-spacing: 5px; margin-top: 7px; padding-left: 5px; }

  /* Frame */
  .frame-line { position: absolute; background: var(--ink); }
  .frame-line--top { left: 110px; top: 18px; width: 722px; height: 2px; }
  .frame-line--bottom { left: 110px; top: 522px; width: 722px; height: 2px; }
  .frame-line--left { left: 18px; top: 108px; width: 2px; height: 321px; }
  .frame-line--right { left: 925px; top: 108px; width: 2px; height: 321px; }
  .divider { position: absolute; left: 571px; top: 92px; width: 2px; height: 362px; background: var(--ink); }

  .ornament {
    position: absolute;
    width: 76px;
    height: 74px;
    background: linear-gradient(135deg, var(--ornament), rgba(255,255,255,0.15));
  }
  .ornament--tl { left: 16px; top: 18px; border-radius: 0 0 60px 0; }
  .ornament--tr { right: 18px; top: 18px; border-radius: 0 0 0 60px; }
  .ornament--bl { left: 16px; bottom: 16px; border-radius: 0 60px 0 0; }
  .ornament--br { right: 18px; bottom: 16px; border-radius: 60px 0 0 0; }

  /* Identity */
  .identity { position: absolute; left: 86px; top: 94px; }
  .identity__name {
    font-family: "Advent Pro", sans-serif;
    font-weight: 300;
    font-size: 48px;
    line-height: 50px;
    letter-spacing: 0.5px;
  }
  .identity__title {
    font-family: "Arimo", sans-serif;
    font-size: 18px;
    line-height: 20px;
    margin-top: -2px;
  }
  .identity__rule {
    position: absolute;
    left: 103px;
    top: 190px;
    width: 248px;
    height: 2px;
    background: linear-gradient(to right, rgba(255,255,255,0), var(--ink) 30%, var(--ink) 70%, rgba(255,255,255,0));
  }

  /* Contacts */
  .contacts { list-style: none; }
  .contact {
    position: absolute;
    left: 80px;
    display: flex;
    align-items: center;
    height: 26px;
    transform: translateY(-50%);
    font-family: "Open Sans", sans-serif;
    font-size: 20px;
    white-space: nowrap;
  }
  .contact__icon { width: 20px; height: 20px; margin-right: 11px; flex: none; }
  .contact--phone { top: 263px; }
  .contact--email { top: 319px; }
  .contact--address { top: 374px; }
  .contact--web { top: 432px; }
</style>
</head>
<body>
<div class="canvas">

  <section class="card card--front" aria-label="Card front">
    <div class="wordmark">
      <span class="wordmark__name">OWEN TASKER</span>
      <span class="wordmark__sub">STUDIOS</span>
    </div>
  </section>

  <section class="card card--back" aria-label="Card back">
    <div class="frame-line frame-line--top"></div>
    <div class="frame-line frame-line--bottom"></div>
    <div class="frame-line frame-line--left"></div>
    <div class="frame-line frame-line--right"></div>
    <div class="divider"></div>

    <div class="ornament ornament--tl" role="img" aria-label="Filigree corner ornament"></div>
    <div class="ornament ornament--tr" role="img" aria-label="Filigree corner ornament"></div>
    <div class="ornament ornament--bl" role="img" aria-label="Filigree corner ornament"></div>
    <div class="ornament ornament--br" role="img" aria-label="Filigree corner ornament"></div>

    <div class="identity">
      <h1 class="identity__name">OWEN TASKER</h1>
      <p class="identity__title">PHOTOGRAPHER</p>
    </div>
    <div class="identity__rule"></div>

    <ul class="contacts">
      <li class="contact contact--phone">
        <svg class="contact__icon" viewBox="0 0 24 24" aria-hidden="true"><path fill="#fff" d="M6.6 10.8a15.1 15.1 0 0 0 6.6 6.6l2.2-2.2c.3-.3.7-.4 1-.2 1.1.4 2.3.6 3.6.6.6 0 1 .4 1 1V20c0 .6-.4 1-1 1A17 17 0 0 1 3 4c0-.6.4-1 1-1h3.5c.6 0 1 .4 1 1 0 1.3.2 2.5.6 3.6.1.3 0 .7-.2 1z"/></svg>
        <span>323-481-5206</span>
      </li>
      <li class="contact contact--email">
        <svg class="contact__icon" viewBox="0 0 24 24" aria-hidden="true"><rect x="2" y="5" width="20" height="14" fill="#fff"/><path d="M2 5l10 8 10-8M2 19l7.5-7M22 19l-7.5-7" stroke="#555" stroke-width="1.5" fill="none"/></svg>
        <span>owentaskerlens@mailbox-example.net</span>
      </li>
      <li class="contact contact--address">
        <svg class="contact__icon" viewBox="0 0 24 24" aria-hidden="true"><path fill="#fff" d="M12 2a7 7 0 0 0-7 7c0 5 7 13 7 13s7-8 7-13a7 7 0 0 0-7-7zm0 9.5a2.5 2.5 0 1 1 0-5 2.5 2.5 0 0 1 0 5z"/></svg>
        <span>Address, Street, City</span>
      </li>
      <li class="contact contact--web">
        <svg class="contact__icon" viewBox="0 0 24 24" aria-hidden="true"><g fill="none" stroke="#fff" stroke-width="1.8"><circle cx="12" cy="12" r="9"/><ellipse cx="12" cy="12" rx="4" ry="9"/><path d="M3 12h18M4.5 7.5h15M4.5 16.5h15"/></g></svg>
        <span>http://taskerlens.examplefolio.net</span>
      </li>
    </ul>

    <div class="wordmark">
      <span class="wordmark__name">OWEN TASKER</span>
      <span class="wordmark__sub">STUDIOS</span>
    </div>
  </section>

</div>
</body>
</html>
```